Business Card Design

New business, starting out small. High end residential/ commercial building company in Sydney Australia's prestigious Eastern suburbs, perfection is our motto and we want our marketing design to reflect that.

Therefore marketing towards high end clients. Looking for design concepts that will portray this image and will appeal to both male and females, prototype has been included- see images. Although we are open to ideas we have included this to give direction.

DARK Navy and white is the colour scheme, as per image provided. Logo ideas welcomed, however design is preferred simple, modern and sophisticated.

This business card will be the template and inspiration for website, t-shirt, banners etc to come so if you want the business, show us your design!

Industry/Entity Type

Marketing

Contact Information for Business Card

Company name: Tallow Ridge Building
Catch phrase: Your vision
Owner/operator: Garreth Pell
Phone: 0468172905
Website: www.tallowridgebuilding.com.au
Licence No 518294K
ABN 72 913 804
Email address
(displayed on back of card):info@tallowridgebuilding.com.au

```html
<!DOCTYPE html>
<html lang="en">
<head>
<meta charset="utf-8">
<title>Tallow Ridge Building — Business Card</title>
<link rel="stylesheet" href="https://fonts.googleapis.com/css2?family=Cinzel:wght@400;500;600&display=swap">
<style>
  :root {
    --page: #ffffff;
    --card-dark: #050505;
    --card-light: #ffffff;
    --gold: #b8902f;
    --ink: #1a1a1a;
    --grey: #6e6e6e;
    --grey-light: #9a9a9a;
    --white: #ffffff;
    --rule: #8a8a8a;
  }
  * { margin: 0; padding: 0; box-sizing: border-box; }
  html, body {
    width: 1200px; height: 900px; overflow: hidden;
    background: var(--page);
    font-family: "Cinzel", serif;
  }
  .canvas { position: relative; width: 1200px; height: 900px; }

  /* Front */
  .card-front {
    position: absolute; left: 312px; top: 104px; width: 576px; height: 334px;
    background: var(--card-dark);
  }
  .front-texture {
    position: absolute; inset: 0;
    background: radial-gradient(ellipse at 50% 45%, #2f2f2f 0%, #161616 45%, #050505 80%);
  }
  .front-frame {
    position: absolute; left: 13px; top: 14px; width: 550px; height: 307px;
    border: 1.5px solid var(--gold);
  }
  .front-title {
    position: absolute; left: 0; right: 0; top: 136px;
    text-align: center; color: var(--white); line-height: 1;
  }
  .front-title .company-line { display: block; font-size: 34px; letter-spacing: 0.5px; }
  .front-title .company-word { display: block; font-size: 38px; font-weight: 500; margin-top: 8px; }
  .front-tagline {
    position: absolute; left: 0; right: 0; top: 223px;
    text-align: center; color: var(--grey); font-size: 15px;
  }
  .front-licence {
    position: absolute; left: 0; right: 0; top: 303px;
    text-align: center; color: #bdbdbd; font-size: 8px; letter-spacing: 0.3px;
  }

  /* Back */
  .card-back {
    position: absolute; left: 312px; top: 464px; width: 574px; height: 326px;
    background: var(--card-light); border: 1px solid var(--rule); overflow: hidden;
  }
  .back-texture {
    position: absolute; inset: 0;
    background: linear-gradient(180deg, #f6f6f6 0%, #fbfbfb 60%, #f4f4f4 100%);
  }
  .back-visual {
    position: absolute; left: 352px; top: 54px; width: 200px; height: 206px;
    background: radial-gradient(ellipse at 55% 55%, #e2e4e6 0%, #eef0f1 50%, rgba(246,246,246,0) 80%);
  }
  .back-tagline {
    position: absolute; left: 0; right: 0; top: 18px;
    text-align: center; color: var(--grey); font-size: 14px;
  }
  .divider {
    position: absolute; left: 304px; top: 50px; width: 3px; height: 228px;
    background: var(--gold);
  }
  .person {
    position: absolute; right: 289px; top: 132px; text-align: right;
  }
  .person-name { color: var(--gold); font-size: 30px; line-height: 1; white-space: nowrap; }
  .person-role { color: var(--grey); font-size: 11px; margin-top: 3px; }
  .contact-row { position: absolute; left: 322px; display: flex; align-items: center; }
  .contact-row svg { width: 34px; height: 34px; flex: none; }
  .contact-phone { top: 119px; }
  .contact-phone .contact-text { font-size: 25px; color: var(--grey); margin-left: 2px; }
  .contact-email { top: 171px; }
  .contact-email .contact-text { font-size: 9px; color: var(--grey); margin-left: 6px; }
  .corner-mark { position: absolute; left: 14px; top: 251px; }
  .website {
    position: absolute; left: 0; right: 0; top: 292px;
    text-align: center; font-size: 15px; color: var(--ink); padding-right: 76px; padding-left: 70px;
  }
  .website .domain { color: var(--gold); }
</style>
</head>
<body>
<main class="canvas">

  <section class="card-front" aria-label="Card front">
    <div class="front-texture" role="img" aria-label="Dark hexagonal metal mesh texture"></div>
    <div class="front-frame"></div>
    <h1 class="front-title">
      <span class="company-line">Tallow Ridge</span>
      <span class="company-word">BUILDING</span>
    </h1>
    <p class="front-tagline">‘Your Vision’</p>
    <p class="front-licence">Licence No 518294K ABN 72 913 804</p>
  </section>

  <section class="card-back" aria-label="Card back">
    <div class="back-texture" role="img" aria-label="Faint white hexagon pattern"></div>
    <div class="back-visual" role="img" aria-label="Faint rendering of a curved modern tower"></div>
    <p class="back-tagline">‘Your Vision’</p>
    <div class="divider"></div>

    <div class="person">
      <p class="person-name">Garreth Pell</p>
      <p class="person-role">Owner/Operator</p>
    </div>

    <div class="contact-row contact-phone">
      <svg viewBox="0 0 34 34" aria-hidden="true">
        <circle cx="17" cy="17" r="15.5" fill="none" stroke="#555" stroke-width="2"/>
        <path d="M11.5 9.5c1-.8 2-.6 2.6.4l1.6 2.8c.5.9.3 1.7-.5 2.3l-1 .7c.7 2 2 3.6 3.8 4.9l.9-.9c.7-.7 1.6-.8 2.4-.2l2.6 1.9c.9.7 1 1.6.2 2.5l-1.2 1.3c-1.3 1.3-3.5 1.1-6-.8-3.3-2.5-5.8-6.2-6.7-9.6-.6-2.3-.1-4 1.3-5.3z" fill="#555"/>
      </svg>
      <span class="contact-text">+1-778-5550148</span>
    </div>

    <div class="contact-row contact-email">
      <svg viewBox="0 0 34 34" aria-hidden="true">
        <circle cx="17" cy="17" r="15.5" fill="#555"/>
        <rect x="8.5" y="11" width="17" height="12" fill="#fff"/>
        <path d="M8.5 11l8.5 7 8.5-7" fill="none" stroke="#555" stroke-width="1.3"/>
      </svg>
      <span class="contact-text">info@tallowridgebuilding.com.au</span>
    </div>

    <svg class="corner-mark" width="50" height="58" viewBox="0 0 50 58" aria-hidden="true">
      <polygon points="0,0 50,58 0,58" fill="#3a3a3a"/>
    </svg>

    <p class="website">www.<span class="domain">tallowridgebuilding</span>.com.au</p>
  </section>

</main>
</body>
</html>
```